Whimsical Business Card Design

We would like a fun and whimsically designed business card. We are a business out of British Columbia and we make creatively designed soaps, shampoo, conditioner, body lotion, massage oil, and essential oil blends mainly for women. We use all natural ingredients scented with essential oils. I would like the design to be girlie, fun, whimsical with character drawings of a shorter white haired lady (my mother) typical short (5'5") grey haired adorable classy granny with dainty pearl earings, and a younger lady (me) taller (5'8") with shoulder length brown layered hair that flips up in the layers (been told I look similar to Helen Voss - modern drop earrings. We can be throwing bubbles, holding each other with one arm and displaying our swirled designer soap in the other hand with bubbles floating, or blowing bubbles at each other, with or without an apron, looking like we are having fun! We are both practical jokers and love to have a good time. This business is very fun! . My favourite colours are teal, bluegreen, ocean blue, pink, lime green for fun colours. If you have a better design in mind I am open. Thanks team!cards I like ID: ID 1042314 - whimsicalID: 1206792 (brown dot) like the colours and character drawing

Target Market(s)

Younger to middle aged

Industry/Entity Type

Skin Care Product

Contact Information for Business Card

Wendy & Fizz
Bath & Body Essentials
Marla Despins
Tidewell Harbour
604-287-3190

Font styles to use
Decorative

Colors
acd036
33a6d7
fbed22
e667a6

Requirements
Must have
• Fun and whimsical theme
Nice to have
• I would like the design to be girlie, fun, whimsical with character drawings of a shorter white haired lady (my mother) typical short (5'5") grey haired adorable classy granny with dainty pearl earings, and a younger lady (me) taller (5'8") with shoulder length brown layered hair that flips up in the layers (been told I look similar to Helen Voss - modern drop earrings. We can be throwing bubbles, holding each other with one arm and displaying our swirled designer soap in the other hand with bubbles floating, or blowing bubbles at each other, with or without an apron, looking like we are having fun! We are both practical jokers and love to have a good time. This business is very fun! . My favourite colours are teal, bluegreen, ocean blue, pink, lime green for fun colours. If you have a better design in mind I am open. Thanks team!cards I like ID: ID 1042314 - whimsicalID: 1206792 (brown dot) like the colours and character drawing

```html
<!DOCTYPE html>
<html lang="en">
<head>
<meta charset="utf-8">
<title>Wendy &amp; Fizz – Business Card</title>
<link rel="stylesheet" href="https://fonts.googleapis.com/css2?family=Sniglet:wght@800&family=Milonga&family=Quattrocento:wght@400;700&display=swap">
<style>
  :root {
    --backdrop: #efece6;
    --card-top: #fbe4e6;
    --card-bottom: #f5bfc5;
    --frame: #d56b7b;
    --frame-halo: #eeb0b8;
    --panel: #ffffff;
    --ink: #2f2a2b;
    --rose: #d6707f;
    --bubble-pink: #f6c6cc;
    --bubble-blue: #a9dbf2;
  }
  * { margin: 0; padding: 0; box-sizing: border-box; }
  html, body { width: 1200px; height: 944px; overflow: hidden; }
  body { background: var(--backdrop); position: relative; }

  .card {
    position: absolute;
    top: 142px;
    width: 402px;
    height: 668px;
    border-radius: 28px;
    overflow: hidden;
    background: linear-gradient(180deg, var(--card-top) 0%, var(--card-top) 35%, var(--card-bottom) 100%);
    box-shadow: 0 3px 8px rgba(0,0,0,0.18);
  }
  .card--front { left: 163px; }
  .card--back { left: 636px; }

  .card__frame { position: absolute; inset: 0; }

  .card__text { position: absolute; left: 0; width: 100%; text-align: center; white-space: nowrap; }

  .front__illustration {
    position: absolute;
    left: 62px; top: 118px;
    width: 276px; height: 248px;
    border-radius: 40% 40% 30% 30%;
    background: radial-gradient(ellipse at 50% 55%, #eef4f8 0%, #dbeef8 45%, #f7e3e6 75%, rgba(255,255,255,0) 100%);
  }
  .front__name {
    top: 398px;
    font-family: "Sniglet", "Comic Sans MS", cursive;
    font-weight: 800;
    font-size: 37px;
    color: var(--ink);
  }
  .front__tagline {
    top: 472px;
    font-family: "Milonga", Georgia, serif;
    font-size: 25px;
    color: var(--ink);
  }

  .back__bubbles {
    position: absolute;
    left: 110px; width: 190px; height: 36px;
    border-radius: 18px;
    background: radial-gradient(ellipse at 50% 50%, var(--bubble-pink) 0%, rgba(246,198,204,0.4) 60%, rgba(255,255,255,0) 100%);
  }
  .back__bubbles--top { top: 80px; }
  .back__bubbles--bottom { top: 508px; left: 80px; width: 250px; height: 40px; }

  .back__name {
    top: 148px;
    font-family: "Sniglet", "Comic Sans MS", cursive;
    font-weight: 800;
    font-size: 38px;
    color: var(--rose);
  }
  .back__tagline {
    top: 207px;
    font-family: "Quattrocento", Georgia, serif;
    font-size: 24px;
    color: var(--ink);
  }
  .back__divider { position: absolute; left: 106px; top: 250px; }
  .back__person {
    top: 284px;
    font-family: "Quattrocento", Georgia, serif;
    font-weight: 700;
    font-size: 23px;
    color: var(--ink);
  }
  .back__icon { position: absolute; left: 186px; }
  .back__icon--phone { top: 330px; }
  .back__icon--pin { top: 424px; }
  .back__phone, .back__city {
    font-family: "Quattrocento", Georgia, serif;
    font-size: 23px;
    color: var(--ink);
    letter-spacing: 1px;
  }
  .back__phone { top: 375px; }
  .back__city { top: 466px; letter-spacing: 0.3px; }
</style>
</head>
<body>

  <section class="card card--front">
    <svg class="card__frame" width="402" height="668" viewBox="0 0 402 668" aria-hidden="true">
      <path d="M44,46 H358 A26,26 0 0 0 384,72 V305 Q384,333 396,333 Q384,333 384,361 V594 A26,26 0 0 0 358,620 H44 A26,26 0 0 0 18,594 V361 Q18,333 6,333 Q18,333 18,305 V72 A26,26 0 0 0 44,46 Z"
            fill="var(--panel)" stroke="var(--frame-halo)" stroke-width="17"/>
      <path d="M44,46 H358 A26,26 0 0 0 384,72 V305 Q384,333 396,333 Q384,333 384,361 V594 A26,26 0 0 0 358,620 H44 A26,26 0 0 0 18,594 V361 Q18,333 6,333 Q18,333 18,305 V72 A26,26 0 0 0 44,46 Z"
            fill="var(--panel)" stroke="var(--frame)" stroke-width="9"/>
    </svg>
    <div class="front__illustration" role="img" aria-label="Illustration of two women in a clawfoot bathtub full of bubbles, holding up handfuls of pink and blue bubbles"></div>
    <h1 class="card__text front__name">Wendy &amp; Fizz</h1>
    <p class="card__text front__tagline">Bath &amp; Body Essentials</p>
  </section>

  <section class="card card--back">
    <svg class="card__frame" width="402" height="668" viewBox="0 0 402 668" aria-hidden="true">
      <path d="M44,46 H358 A26,26 0 0 0 384,72 V305 Q384,333 396,333 Q384,333 384,361 V594 A26,26 0 0 0 358,620 H44 A26,26 0 0 0 18,594 V361 Q18,333 6,333 Q18,333 18,305 V72 A26,26 0 0 0 44,46 Z"
            fill="var(--panel)" stroke="var(--frame-halo)" stroke-width="17"/>
      <path d="M44,46 H358 A26,26 0 0 0 384,72 V305 Q384,333 396,333 Q384,333 384,361 V594 A26,26 0 0 0 358,620 H44 A26,26 0 0 0 18,594 V361 Q18,333 6,333 Q18,333 18,305 V72 A26,26 0 0 0 44,46 Z"
            fill="var(--panel)" stroke="var(--frame)" stroke-width="9"/>
    </svg>
    <div class="back__bubbles back__bubbles--top" role="img" aria-label="Cluster of floating pink bubbles"></div>
    <h2 class="card__text back__name">Wendy &amp; Fizz</h2>
    <p class="card__text back__tagline">Bath &amp; Body Essentials</p>
    <svg class="back__divider" width="190" height="20" viewBox="0 0 190 20" aria-hidden="true">
      <path d="M2,4 Q20,12 80,12 Q92,12 95,18 Q98,12 110,12 Q170,12 188,4" fill="none" stroke="var(--rose)" stroke-width="2.5" stroke-linecap="round"/>
    </svg>
    <p class="card__text back__person">Marla Despins</p>
    <svg class="back__icon back__icon--phone" width="30" height="30" viewBox="0 0 30 30" aria-hidden="true">
      <circle cx="15" cy="15" r="13" fill="none" stroke="var(--ink)" stroke-width="1.6"/>
      <path d="M10.5,8 L13,8 L14,11.5 L12.5,13 Q14,16.5 17,17.5 L18.5,16 L22,17 L22,19.5 Q21,22 18,21.5 Q10,19.5 8.5,11.5 Q8.5,8.5 10.5,8 Z" fill="var(--ink)"/>
    </svg>
    <p class="card__text back__phone">604-287-3190</p>
    <svg class="back__icon back__icon--pin" width="30" height="30" viewBox="0 0 30 30" aria-hidden="true">
      <circle cx="15" cy="15" r="13" fill="none" stroke="var(--ink)" stroke-width="1.6"/>
      <path d="M15,23 Q9.5,16 9.5,12.5 A5.5,5.5 0 0 1 20.5,12.5 Q20.5,16 15,23 Z" fill="var(--ink)"/>
      <circle cx="15" cy="12.5" r="2.2" fill="var(--panel)"/>
    </svg>
    <p class="card__text back__city">Tidewell Harbour</p>
    <div class="back__bubbles back__bubbles--bottom" role="img" aria-label="Row of floating pink bubbles"></div>
  </section>

</body>
</html>
```